Business card design needed

Chasing a very simplistic modern design with a logo incorporating "TRV".
I'm starting a plumbing business.
I do water, sanitary and drainage plumbing that will cover residential, commercial, rental, rural, excavation, new housing and all maintanence requirements.

Industry/Entity Type

Business

Contact Information for Business Card

TRV PLUMBING SERVICES
DEAN HOLLOWBY - LICENSED PLUMBER
PHONE: 0481926574
E-MAIL: hollodt7@wirelane.com
NORTHERN SUBURBS

Requirements
Must have
• lower case email address

```html
<!DOCTYPE html>
<html lang="en">
<head>
<meta charset="utf-8">
<title>TRV Plumbing Services – Business Card</title>
<link rel="stylesheet" href="https://fonts.googleapis.com/css2?family=Saira:wght@400;600;700&display=swap">
<style>
  :root {
    --page: #e9e9e6;
    --charcoal: #39393b;
    --charcoal-deep: #2e2e30;
    --brand-blue: #2a93cf;
    --card-light: #e6e8ea;
    --card-white: #f4f5f6;
    --ink: #2b2b2d;
    --ink-soft: #4a4a4d;
    --white: #ffffff;
  }
  * { box-sizing: border-box; margin: 0; padding: 0; }
  html, body {
    width: 1200px; height: 880px; overflow: hidden;
    background: var(--page);
    font-family: "Saira", sans-serif;
  }
  .canvas {
    width: 1200px; height: 880px;
    display: flex; flex-direction: column;
    align-items: center; justify-content: center;
    gap: 44px;
  }
  .card {
    position: relative;
    width: 640px; height: 366px;
    border-radius: 6px;
    overflow: hidden;
    box-shadow: 0 6px 18px rgba(0,0,0,.18);
  }

  /* Front */
  .card-front { background: var(--card-light); }
  .card-front .brand-panel {
    position: absolute; left: 0; top: 0; right: 0; height: 230px;
    background: linear-gradient(180deg, var(--charcoal) 0%, var(--charcoal-deep) 100%);
  }
  .card-front .brand-rule {
    position: absolute; left: 0; right: 0; top: 230px; height: 10px;
    background: var(--brand-blue);
  }
  .card-front .lockup {
    position: absolute; left: 70px; top: 34px;
    color: var(--brand-blue); font-weight: 600;
  }
  .lockup .mark-square {
    display: inline-block; width: 22px; height: 22px;
    background: var(--brand-blue); margin-right: 14px; vertical-align: 14px;
  }
  .card-front .lockup-name { font-size: 84px; line-height: 1; letter-spacing: 4px; }
  .card-front .lockup-trade { font-size: 46px; line-height: 1.1; margin-top: 4px; }
  .card-front .tagline {
    position: absolute; left: 0; right: 0; top: 240px; bottom: 0;
    display: flex; align-items: center; justify-content: center; gap: 20px;
    font-weight: 700; font-size: 22px; letter-spacing: 2.6px; color: var(--ink);
  }
  .tagline .dot { width: 9px; height: 9px; border-radius: 50%; background: var(--ink); }

  /* Back */
  .card-back { background: var(--card-white); }
  .card-back .brand-panel {
    position: absolute; left: 0; top: 0; right: 0; height: 92px;
    background: linear-gradient(180deg, var(--charcoal) 0%, var(--charcoal-deep) 100%);
  }
  .card-back .brand-rule {
    position: absolute; left: 0; right: 0; top: 92px; height: 7px;
    background: var(--brand-blue);
  }
  .card-back .lockup {
    position: absolute; right: 40px; top: 24px;
    font-size: 36px; line-height: 1.2; font-weight: 600;
    color: var(--brand-blue); white-space: nowrap;
  }
  .card-back .side-tab {
    position: absolute; left: 0; top: 136px; width: 10px; height: 52px;
    background: var(--brand-blue); border-radius: 0 6px 6px 0;
  }
  .contact { position: absolute; left: 48px; top: 132px; }
  .contact .person-name { font-size: 26px; font-weight: 700; color: var(--ink); line-height: 1.2; }
  .contact .person-role { font-size: 22px; font-weight: 400; color: var(--ink-soft); line-height: 1.3; }
  .contact .details { margin-top: 22px; font-size: 22px; line-height: 1.35; color: var(--ink); }
  .contact .label { color: var(--brand-blue); }
</style>
</head>
<body>
<main class="canvas">

  <section class="card card-front" aria-label="Business card front">
    <div class="brand-panel"></div>
    <div class="brand-rule"></div>
    <div class="lockup">
      <div class="lockup-name"><span class="mark-square"></span>TRV</div>
      <div class="lockup-trade">Plumbing Services</div>
    </div>
    <div class="tagline">
      <span>Licensed Plumber</span>
      <span class="dot"></span>
      <span>Northern Suburbs</span>
    </div>
  </section>

  <section class="card card-back" aria-label="Business card back">
    <div class="brand-panel"></div>
    <div class="brand-rule"></div>
    <div class="lockup">TRV Plumbing Services</div>
    <div class="side-tab"></div>
    <div class="contact">
      <p class="person-name">Dean Hollowby</p>
      <p class="person-role">Licensed Plumber</p>
      <div class="details">
        <p><span class="label">Phone:</span> 0481.926.574</p>
        <p><span class="label">E-mail:</span> hollodt7@wirelane.com</p>
      </div>
    </div>
  </section>

</main>
</body>
</html>
```